Icon Design Project: Create 5 icons to represent our companies 5 sectors.

We are Lumen Pressworks, a leading multi-fascited print production company looking for 5 icons to help promote our services across all media’s.

OUR ELEVATOR PITCH:
Do you just wish you could trust one company to do it all well?
Relax. You can. We got it covered. You have so many relationships to maintain, accounts to manage and decisions to make. Wouldn't life be easier if you could trust just one company to understand your brand and integrate it into your print, sign, display, apparel and promotional marketing well?
With Lumen Pressworks you can. Relax, we’ve got it covered.

OUR REQUEST:
We are looking for 5 icons/symbols to be used in our print and signage material as well as on our new website.

The 5 sectors and colours we use to represent each is as follows:
PRINT - Yellow: C4 M0 Y93 K0
SIGNS - Orange: C0 M60 Y100 K0
DISPLAY - Pink: C0 M100 Y0 K0
PROMOTIONAL - Purple: C65 M95 Y0 K0
APPAREL - Green: C55 M0 Y100 K0

The icon backgrounds could be these colours with a simple black/white pictogram on them, or they could have a clear background with the pictograms in the colours.

Within each of our services we produce the following:

PRINT business cards, comp slips, business forms, envelopes, stickers
brochures, greeting cards, posters, letterhead, pads, carbonless books labels, flyers, postcards, invites

SIGNS permanent, temporary, vehicles, 3-d, post 'n' panel, buildings, pylons, magnetic, illuminated, banners, blackboards, window graphics,
whiteboards, pavement signs,

DISPLAY banner stands, roll-ups, pop-up counters and towers, brochure and catalogue stands flags, display walls, poster stands and frames,
display lighting, canvas printing,

PROMOTIONAL pens, umbrellas, calculators, confectionary, keyrings, bathroom, leisure, desktop, tools, magnets, clocks, drinkware, personal gifts, sports, golf, conference, lights

APPAREL screen printing, embroidery and rubber based transferring, plus supply of a massive clothing range of tee-shirts, polos, caps, beanies, jerseys, corporate and high vis workwear,

GUIDELINES:
The icons will need to be vector based icons/pictograms and should be simple, clear and easily identifiable. They will be used in conjunction with our logo in our printed marketing material as well as for navigation on our new website and as large signs on our building, and in other media’s as required. I have uploaded our new letterhead, Invoice and Statement design to give you a feel for our brand.

Good Luck!

Target Market(s)

All business owners in New Zealand, and the pacific islands

Industry/Entity Type

Embroidery

Requirements
Nice to have
• Icons could show a couple of each of the listed items. Eg. Print may show a business card and a letterhead. Display may show a flag and a rollup banner stand.

```html
<!DOCTYPE html>
<html lang="en">
<head>
<meta charset="utf-8">
<title>Lumen Pressworks – Sector Icons</title>
<link rel="stylesheet" href="https://fonts.googleapis.com/css2?family=Tinos&display=swap">
<style>
  :root {
    --canvas: #ffffff;
    --band: #6b5d51;
    --print: #f2f20f;
    --signs: #ff6a00;
    --display: #ff00ff;
    --promotional: #7a12ff;
    --apparel: #7fff00;
    --pictogram: #ffffff;
  }
  * { margin: 0; padding: 0; box-sizing: border-box; }
  html, body {
    width: 1200px;
    height: 273px;
    overflow: hidden;
    background: var(--canvas);
  }
  .icon-band {
    position: relative;
    width: 1196px;
    height: 273px;
    background: var(--band);
    border-radius: 26px;
    font-family: "Tinos", "Times New Roman", serif;
  }
  .sector {
    position: absolute;
    width: 200px;
    text-align: center;
  }
  .sector__tile {
    display: block;
    width: 200px;
    height: 198px;
    border-radius: 28px;
  }
  .sector__label {
    position: absolute;
    left: -30px;
    right: -30px;
    font-size: 26px;
    line-height: 1;
    white-space: nowrap;
  }
  .sector__glyph {
    fill: var(--pictogram);
  }
  .sector__letters {
    fill: var(--pictogram);
    font-family: "Tinos", "Times New Roman", serif;
    font-size: 112px;
  }

  .sector--print { left: 36px; top: 31px; }
  .sector--print .sector__tile { background: var(--print); }
  .sector--print .sector__label { color: var(--print); top: 205px; }

  .sector--signs { left: 261px; top: 25px; }
  .sector--signs .sector__tile { background: var(--signs); }
  .sector--signs .sector__label { color: var(--signs); top: 210px; left: -32px; right: -28px; }

  .sector--display { left: 492px; top: 27px; }
  .sector--display .sector__tile { background: var(--display); }
  .sector--display .sector__label { color: var(--display); top: 210px; left: -26px; right: -34px; }

  .sector--promotional { left: 723px; top: 25px; }
  .sector--promotional .sector__tile { background: var(--promotional); }
  .sector--promotional .sector__label { color: var(--promotional); top: 211px; left: -22px; right: -38px; }

  .sector--apparel { left: 950px; top: 23px; }
  .sector--apparel .sector__tile { background: var(--apparel); }
  .sector--apparel .sector__label { color: var(--apparel); top: 211px; left: -38px; right: -22px; }
</style>
</head>
<body>
<main class="icon-band">

  <section class="sector sector--print">
    <svg class="sector__tile" viewBox="0 0 200 198" aria-label="Print icon">
      <text class="sector__letters" x="100" y="133" text-anchor="middle">Aa</text>
    </svg>
    <p class="sector__label">Print</p>
  </section>

  <section class="sector sector--signs">
    <svg class="sector__tile" viewBox="0 0 200 198" aria-label="Signs icon">
      <polygon class="sector__glyph" points="73,42 126,42 164,78 164,124 126,162 73,162 37,124 37,78"/>
      <rect class="sector__glyph" x="92" y="158" width="17" height="40"/>
    </svg>
    <p class="sector__label">Signs</p>
  </section>

  <section class="sector sector--display">
    <svg class="sector__tile" viewBox="0 0 200 198" aria-label="Display icon">
      <polygon class="sector__glyph" points="26,38 63,58 63,158 26,140"/>
      <rect class="sector__glyph" x="69" y="59" width="62" height="101"/>
      <polygon class="sector__glyph" points="136,58 174,38 174,140 136,158"/>
    </svg>
    <p class="sector__label">Display</p>
  </section>

  <section class="sector sector--promotional">
    <svg class="sector__tile" viewBox="0 0 200 198" aria-label="Promotional icon">
      <path class="sector__glyph" d="M62 52 H154 V156 Q154 165 145 165 H71 Q62 165 62 156 Z"/>
      <path class="sector__glyph" fill-rule="evenodd" d="M28 74 H66 V134 H28 Z M42 89 V119 H62 V89 Z"/>
    </svg>
    <p class="sector__label">Promotional</p>
  </section>

  <section class="sector sector--apparel">
    <svg class="sector__tile" viewBox="0 0 200 198" aria-label="Apparel icon">
      <path class="sector__glyph" d="M82 45 Q100 58 120 45 L168 64 L156 92 L140 86 L140 170 L68 172 L68 86 L50 93 L38 65 Z"/>
    </svg>
    <p class="sector__label">Apparel</p>
  </section>

</main>
</body>
</html>
```